Lantern over The Moor Business Card Design

Simple 2 sided card ideally based around a zen garden approach (larger stone in a sand combed garden), but not essential.
Business is Project Management, IT Consultancy, Business Analysis.
Initially one person, however others may join the business so a unique logo would be preferred that encapsulates the approach of one pebble dropping in water causing many ripples. Potentially based around a zen garden, but not essential.
Clean and tidy, double sided, glossy, interesting and unique.
Company Name and contact details on one side (with the ability to replace the name, telephone and email address for more staff):
Lantern over The Moor Ltd
Derek Holbrook
077 5182 6207
derek@lanternoverthemoor.example
Company name and offering on the other:
Lantern over The Moor Ltd
Project Management
Business Analysis
IT Consultancy
Interesting looking font, nice colours, not too many, but simple, effective and eye catching.
Potential Image either as a background or to the left/ right. Replicated on the rear of the card.
Design once approved and complete to be the sole property of Lantern over The Moor Ltd.
No requirement for Twitter, Facebook or Linked in details on any design
Lantern over The Moor
Derek Holbrook
077 5182 6207
Project Management
Business Analysis
IT Consultancy

```html
<!DOCTYPE html>
<html lang="en">
<head>
<meta charset="utf-8">
<title>Lantern over The Moor Business Card Design</title>
<link href="https://fonts.googleapis.com/css2?family=Open+Sans:wght@400;600&display=swap" rel="stylesheet">
<style>
  :root {
    --backdrop: #e9e6e1;
    --paper: #ffffff;
    --ocean-light: #2a8fd6;
    --ocean-mid: #1366b8;
    --ocean-deep: #0a3f86;
    --brand-blue: #1b5fb0;
    --ink-light: #ffffff;
    --rule: rgba(120, 190, 245, 0.55);
    --band: rgba(140, 200, 250, 0.16);
  }
  * { box-sizing: border-box; margin: 0; padding: 0; }
  html, body {
    width: 1200px; height: 913px; overflow: hidden;
    background: var(--backdrop);
    font-family: "Open Sans", Arial, sans-serif;
  }
  .canvas { position: relative; width: 1200px; height: 913px; }
  .card {
    position: absolute; width: 560px; height: 320px; overflow: hidden;
    border-radius: 3px;
    box-shadow: 0 10px 24px rgba(0,0,0,0.22);
  }
  .card--contact { left: 70px; top: 100px; background: var(--paper); }
  .card--offering {
    left: 570px; top: 490px;
    background: radial-gradient(ellipse at 35% 25%, var(--ocean-light) 0%, var(--ocean-mid) 50%, var(--ocean-deep) 100%);
  }
  .contact__sea {
    position: absolute; left: 0; right: 0; top: 128px; bottom: 0;
    background: linear-gradient(160deg, var(--ocean-light) 0%, var(--ocean-mid) 45%, var(--ocean-deep) 100%);
  }
  .offering__band {
    position: absolute; left: 0; right: 0; top: 118px; height: 96px;
    background: linear-gradient(90deg, rgba(140,200,250,0.04) 0%, var(--band) 45%, rgba(140,200,250,0.06) 100%);
    border-top: 1px solid var(--rule);
    border-bottom: 1px solid var(--rule);
  }
  .brand {
    position: absolute; display: flex; align-items: center; gap: 10px;
    font-weight: 600; letter-spacing: 1.5px; text-transform: uppercase;
    white-space: nowrap;
  }
  .brand__dot { width: 14px; height: 14px; border-radius: 50%; flex: none; }
  .card--contact .brand { left: 34px; top: 86px; font-size: 21px; color: var(--brand-blue); }
  .card--contact .brand__dot { background: var(--brand-blue); }
  .card--offering .brand { left: 40px; top: 62px; font-size: 22px; color: var(--ink-light); }
  .card--offering .brand__dot { background: var(--ink-light); }
  .person {
    position: absolute; left: 34px; top: 150px; color: var(--ink-light);
    font-size: 20px;
  }
  .person__role { font-size: 13px; padding-left: 8px; margin-left: 6px; border-left: 1px solid var(--ink-light); }
  .details { position: absolute; left: 34px; top: 196px; right: 40px; list-style: none; color: var(--ink-light); font-size: 13px; }
  .details li { padding: 7px 0; border-top: 1px solid var(--rule); }
  .offering { position: absolute; left: 360px; top: 133px; list-style: none; color: var(--ink-light); font-size: 13px; line-height: 22px; }
  .offering li::before { content: "•"; margin-right: 8px; }
  .registration {
    position: absolute; left: 40px; right: 40px; bottom: 36px;
    padding-top: 10px; border-top: 1px solid var(--rule);
    color: var(--ink-light); font-size: 12px; letter-spacing: .3px;
  }
</style>
</head>
<body>
<main class="canvas">
  <section class="card card--contact" aria-label="Contact side">
    <div class="contact__sea"></div>
    <div class="brand"><span class="brand__dot"></span>Lantern over The Moor Ltd</div>
    <p class="person">Derek Holbrook <span class="person__role">Designation</span></p>
    <ul class="details">
      <li>077 5182 6207</li>
      <li>derek@lanternoverthemoor.example</li>
      <li>www.lanternoverthemoor.example</li>
    </ul>
  </section>

  <section class="card card--offering" aria-label="Offering side">
    <div class="offering__band"></div>
    <div class="brand"><span class="brand__dot"></span>Lantern over The Moor Ltd</div>
    <ul class="offering">
      <li>Project Management</li>
      <li>Business Analysis</li>
      <li>IT Consultancy</li>
    </ul>
    <p class="registration">Company Registration No. 4521907</p>
  </section>
</main>
</body>
</html>
```